Morvela Aesthetic Doctor

I require an elegant, luxurious looking business card for my aesthetic business. I am a doctor and that will set me aside from competitors. I am planning to provide home and spa based treatments to clients with high expectations. I have attached my logo.

```html
<!DOCTYPE html>
<html lang="en">
<head>
<meta charset="utf-8">
<title>Morvela Aesthetic Doctor – Business Card</title>
<link rel="stylesheet" href="https://fonts.googleapis.com/css2?family=Open+Sans:wght@400&display=swap">
<style>
  :root {
    --backdrop: #e4e4e4;
    --card-blue: #1c6ab0;
    --card-white: #f4f4f4;
    --ink: #222222;
    --accent: #1a9ee0;
    --brand-grey: #a7a9ac;
    --white: #ffffff;
    --s1: #1b6fb3;
    --s2: #2384c6;
    --s3: #3a9ad4;
    --s4: #5bb2e0;
    --s5: #7ec7ea;
    --s6: #a0d6ef;
  }
  * { box-sizing: border-box; margin: 0; padding: 0; }
  html, body {
    width: 1200px; height: 960px; overflow: hidden;
    background: var(--backdrop);
    font-family: "Open Sans", Arial, sans-serif;
  }
  .canvas { position: relative; width: 1200px; height: 960px; }
  .card { position: absolute; left: 320px; width: 560px; height: 342px; overflow: hidden; }
  .card--front { top: 119px; background: var(--card-blue); }
  .card--back { top: 498px; background: var(--card-white); }

  .stripe { position: absolute; bottom: 0; height: 15px; display: flex; }
  .stripe span { flex: 1; }
  .card--front .stripe { left: 52px; width: 458px; }
  .card--back .stripe { left: 0; width: 560px; }

  .brand { position: absolute; display: flex; align-items: center; }
  .brand__ring { border-radius: 50%; border: 3px solid var(--brand-grey); flex: none; }
  .brand__name { font-weight: 400; line-height: 1.05; letter-spacing: 0.04em; text-transform: uppercase; }
  .card--front .brand { left: 68px; top: 86px; gap: 28px; }
  .card--front .brand__ring { width: 116px; height: 116px; }
  .card--front .brand__name { color: var(--white); font-size: 34px; }
  .card--front .brand__name small { display: block; font-size: 22px; letter-spacing: 0.06em; }

  .services {
    position: absolute; left: 0; right: 0; top: 238px;
    text-align: center; color: var(--white); font-size: 17px; line-height: 21px;
  }

  .card--back .brand { left: 36px; top: 140px; gap: 14px; }
  .card--back .brand__ring { width: 60px; height: 60px; border-width: 2px; }
  .card--back .brand__name { color: var(--brand-grey); font-size: 20px; }
  .card--back .brand__name small { display: block; font-size: 12px; letter-spacing: 0.06em; }

  .divider { position: absolute; left: 279px; top: 99px; width: 2px; height: 144px; background: var(--accent); }
  .contact { position: absolute; left: 299px; top: 100px; }
  .contact__name { font-size: 19px; color: var(--ink); line-height: 24px; }
  .contact__creds { font-size: 12px; color: var(--accent); }
  .contact__qual { font-size: 14px; color: var(--accent); line-height: 18px; }
  .contact__list { list-style: none; margin-top: 18px; }
  .contact__list li { display: flex; align-items: center; gap: 4px; font-size: 16px; color: var(--ink); line-height: 21px; }
  .contact__list svg { width: 14px; height: 14px; fill: none; stroke: var(--accent); stroke-width: 1.6; }
  .social { position: absolute; left: 0; right: 0; top: 287px; display: flex; justify-content: center; align-items: center; gap: 6px; font-size: 12px; color: var(--accent); }
  .social__dot { width: 14px; height: 14px; border-radius: 50%; background: var(--accent); }
</style>
</head>
<body>
<main class="canvas">
  <section class="card card--front">
    <div class="brand">
      <div class="brand__ring"></div>
      <p class="brand__name">Morvela<small>Aesthetic Doctor</small></p>
    </div>
    <p class="services">
      Dermal injectables - Plasma facials - Microneedling<br>
      Skin boosters - Excessive sweating<br>
      Home and Spa Based Treatments
    </p>
    <div class="stripe">
      <span style="background:var(--s1)"></span><span style="background:var(--s2)"></span><span style="background:var(--s3)"></span><span style="background:var(--s5)"></span><span style="background:var(--s6)"></span><span style="background:var(--s5)"></span><span style="background:var(--s4)"></span><span style="background:var(--s2)"></span><span style="background:var(--s1)"></span>
    </div>
  </section>

  <section class="card card--back">
    <div class="brand">
      <div class="brand__ring"></div>
      <p class="brand__name">Morvela<small>Aesthetic Doctor</small></p>
    </div>
    <div class="divider"></div>
    <div class="contact">
      <p class="contact__name">Dr Elsa Varnik <span class="contact__creds">MRCPCH MD</span></p>
      <p class="contact__qual">Australasian Diploma of<br>Aesthetic Medicine</p>
      <ul class="contact__list">
        <li><svg viewBox="0 0 16 16"><path d="M4 2l2.5 3-1.5 1.5c1 2 2.5 3.5 4.5 4.5L11 9.5l3 2.5-1.5 2C7 14 2 9 2 3.5z"/></svg>0800 555 019</li>
        <li><svg viewBox="0 0 16 16"><rect x="2" y="4" width="12" height="9"/><path d="M2 4l6 5 6-5"/></svg>elsa@morvela.co.nz</li>
        <li><svg viewBox="0 0 16 16"><circle cx="8" cy="8" r="6"/><ellipse cx="8" cy="8" rx="2.6" ry="6"/><path d="M2 8h12"/></svg>www.morvela.co.nz</li>
      </ul>
    </div>
    <div class="social"><span class="social__dot"></span>morvela</div>
    <div class="stripe">
      <span style="background:var(--s1)"></span><span style="background:var(--s1)"></span><span style="background:var(--s2)"></span><span style="background:var(--s3)"></span><span style="background:var(--s5)"></span><span style="background:var(--s6)"></span><span style="background:var(--s5)"></span><span style="background:var(--s4)"></span><span style="background:var(--s2)"></span><span style="background:var(--s1)"></span><span style="background:var(--s1)"></span>
    </div>
  </section>
</main>
</body>
</html>
```